Supplement Bottle Label Design and Creative Lifestyle Images

We are a medical home consumer brand and we are releasing a supplement line of products called "Velbrook Nutrition". We are in need of a supplement bottle design for our supplement line, Velbrook Nutrition. We are looking for a very appealing, simple, and clean design, but with a medical feel to it.

We would like to see designs with a black background as well as designs with a white background. Bottle size will approximately be 200cc and label will about be 7" x 2.5", but this size is subject to change.

We really like the Pirlen Nutrition design and the Gantry Lab, however, we like the medical style of Nutrition Keystones. Please reference the links below.

To start off, the title of this bottle will be "Calm-Spire". We will need all similar warning about FDA, made in USA, non-GMA, GMP, ect. Please use the formula below to start:

2 Pills per serving
Blueberry pterostilbene - 10mg
Bacopa - 150mg
Gingko Biloba - 50mg
Vinpocetine - 10mg
Alpha-GPC -150mg
TAU - 35mg

https://www.shopvarn.example/Pirlen-Nutrition/b/ref=bl_dp_s_web_48213907562?ie=UTF8&node=48213907562&field-lbr_brands_browse-bin=Pirlen+Nutrition

https://www.shopvarn.example/l/7394208156

https://www.shopvarn.example/Nutrition-Keystones/b/ref=bl_dp_s_web_86420531977?ie=UTF8&node=86420531977&field-lbr_brands_browse-bin=Nutrition+Keystones

Industry/Entity Type

Medical

```html
<!DOCTYPE html>
<html lang="en">
<head>
<meta charset="utf-8">
<title>Velbrook Nutrition – Calm-Spire label range</title>
<link rel="stylesheet" href="https://fonts.googleapis.com/css2?family=Oswald:wght@400;500&family=Roboto:wght@400;700&display=swap">
<style>
  :root {
    --page-bg: #f4f5f6;
    --label-bg: #1b1b1c;
    --label-bg-light: #262627;
    --ink-light: #ffffff;
    --ink-muted: #d8d8d8;
    --accent-green: #3cb54a;
    --accent-red: #ec2227;
    --accent-blue: #10a9e8;
  }
  * { margin: 0; padding: 0; box-sizing: border-box; }
  html, body {
    width: 1200px;
    height: 856px;
    overflow: hidden;
    background: var(--page-bg);
  }
  .label-range {
    position: relative;
    width: 1200px;
    height: 856px;
  }
  .label {
    position: absolute;
    top: 288px;
    width: 298px;
    height: 370px;
    background: linear-gradient(135deg, var(--label-bg-light) 0%, var(--label-bg) 55%, #141415 100%);
    color: var(--ink-light);
    overflow: hidden;
  }
  .label--green { left: 108px; --accent: var(--accent-green); }
  .label--red   { left: 451px; --accent: var(--accent-red); }
  .label--blue  { left: 794px; --accent: var(--accent-blue); }

  .label__band-top {
    position: absolute; left: 0; top: 0;
    width: 100%; height: 4px;
    background: var(--accent);
  }
  .label__band-bottom {
    position: absolute; left: 0; bottom: 0;
    width: 100%; height: 8px;
    background: var(--accent);
  }
  .label__count {
    position: absolute;
    top: 0; left: 50%;
    transform: translateX(-50%);
    width: 48px; height: 56px;
    background: var(--accent);
    text-align: center;
    font-family: "Oswald", sans-serif;
    font-weight: 500;
    line-height: 1;
  }
  .label__count-number { display: block; font-size: 28px; padding-top: 4px; }
  .label__count-unit { display: block; font-size: 13px; margin-top: 2px; }

  .label__brand {
    position: absolute;
    top: 116px; left: 0; width: 100%;
    text-align: center;
    font-family: "Oswald", sans-serif;
    font-weight: 500;
    font-size: 29px;
    line-height: 1.2;
    letter-spacing: -0.3px;
    text-transform: uppercase;
  }
  .label__product {
    position: absolute;
    top: 164px; left: 0; width: 100%;
    text-align: center;
    font-family: "Oswald", sans-serif;
    font-weight: 500;
    font-size: 38px;
    line-height: 1.2;
    color: var(--accent);
  }

  .label__tagline {
    position: absolute;
    top: 338px; left: 0; width: 100%;
    text-align: center;
    font-family: "Roboto", sans-serif;
    font-size: 8px;
    color: var(--ink-muted);
    letter-spacing: 0.2px;
  }
  .label__tagline strong { color: var(--ink-light); }
</style>
</head>
<body>
  <main class="label-range">
    <section class="label label--green">
      <div class="label__band-top"></div>
      <div class="label__count"><span class="label__count-number">30</span><span class="label__count-unit">PILLS</span></div>
      <h1 class="label__brand">Velbrook Nutrition</h1>
      <h2 class="label__product">Calm-Spire</h2>
      <p class="label__tagline">LOREM IPSUM PASSAGE USED SINCE THE <strong>1500S</strong></p>
      <div class="label__band-bottom"></div>
    </section>

    <section class="label label--red">
      <div class="label__band-top"></div>
      <div class="label__count"><span class="label__count-number">30</span><span class="label__count-unit">PILLS</span></div>
      <h1 class="label__brand">Velbrook Nutrition</h1>
      <h2 class="label__product">Calm-Spire</h2>
      <p class="label__tagline">LOREM IPSUM PASSAGE USED SINCE THE <strong>1500S</strong></p>
      <div class="label__band-bottom"></div>
    </section>

    <section class="label label--blue">
      <div class="label__band-top"></div>
      <div class="label__count"><span class="label__count-number">30</span><span class="label__count-unit">PILLS</span></div>
      <h1 class="label__brand">Velbrook Nutrition</h1>
      <h2 class="label__product">Calm-Spire</h2>
      <p class="label__tagline">LOREM IPSUM PASSAGE USED SINCE THE <strong>1500S</strong></p>
      <div class="label__band-bottom"></div>
    </section>
  </main>
</body>
</html>
```